Building and Facilities Management brochure

Please refer to attached PDF, page by page with information about the brief.
SOPHISTICATED, BOLD, PROFESSIONAL BROCHURE to market our company in business meetings to Builders, Owners of buildings, Strata Committees etc.

The final design should portray quality, service, integrity,
Clear Communication

Attached is:
- pdf with details of basic layout options and wording and most of the information about the brief.
- Logo options to use
- Business card designs to understand what design we have previously had.
- Word document of the pdf if that helps to copy the information.

Target Market(s)

Professionals. Builders/developer, Strata Owners, and Building owners who want a high level of service and management of their building

Industry/Entity Type

It Company

Requirements
Must have
• - Logo
• - Contact details
• - Use of the colour in the design which has been specified.
• - Images/s of building/s
• - Use the phrase "Quality Service with Integrity"
Nice to have
• - as much of the wording as possible from the document which was uploaded, that will fit and work with the design
Should not have
• Excessive colour or variances as it needs to stay clear, bold and sophisticated.
• Too much on the page, clarity is key for clear communication without trying to clutter too much on the page.

```html
<!DOCTYPE html>
<html lang="en">
<head>
<meta charset="utf-8">
<title>Alder Property Group – Brochure Cover</title>
<link rel="stylesheet" href="https://fonts.googleapis.com/css2?family=Lato:wght@400;700;900&family=Oswald:wght@700&display=swap">
<style>
  :root {
    --slate: #3d4450;
    --sky: #2aa6e0;
    --paper: #ffffff;
    --mist: #e9ebee;
    --ink: #3a3f48;
  }
  html, body { margin: 0; padding: 0; overflow: hidden; background: var(--paper); }
  .canvas { position: relative; width: 1200px; height: 1200px; overflow: hidden; background: var(--paper); font-family: "Lato", sans-serif; }
  .artwork { position: absolute; inset: 0; width: 1200px; height: 1200px; }
  .brand-name { position: absolute; margin: 0; color: var(--sky); font-family: "Lato", sans-serif; font-weight: 900; line-height: 1; text-align: center; letter-spacing: 4px; }
  .brand-name--front { left: 648px; width: 400px; top: 246px; font-size: 96px; }
  .brand-name--back { left: 176px; width: 300px; top: 724px; font-size: 60px; }
  .contact { position: absolute; left: 200px; top: 814px; width: 260px; color: var(--ink); font-size: 12px; line-height: 1.25; }
  .contact-phone { text-align: center; margin: 0 0 12px 0; padding-left: 14px; }
  .contact-row { display: flex; align-items: flex-start; gap: 6px; margin: 0 0 6px 14px; }
  .contact-row svg { flex: none; margin-top: 1px; }
  .contact-phone svg { vertical-align: -1px; margin-right: 2px; }
  .headline { position: absolute; left: 600px; width: 500px; top: 790px; margin: 0; text-align: center; font-family: "Oswald", sans-serif; font-weight: 700; text-transform: uppercase; font-size: 62px; line-height: 56px; letter-spacing: 0.5px; }
  .headline-line { display: block; color: var(--slate); }
  .headline-line--accent { color: var(--sky); }
  .footer-url { position: absolute; top: 928px; width: 400px; margin: 0; text-align: center; color: var(--paper); font-size: 12px; letter-spacing: 3px; }
  .footer-url--back { left: 131px; }
  .footer-url--front { left: 658px; }
</style>
</head>
<body>
<div class="canvas">
  <svg class="artwork" viewBox="0 0 1500 1500" xmlns="http://www.w3.org/2000/svg">
    <defs>
      <linearGradient id="skylineFade" x1="0" y1="0" x2="0" y2="1">
        <stop offset="0" stop-color="#ffffff"/>
        <stop offset="0.45" stop-color="#e4e6e9"/>
        <stop offset="0.75" stop-color="#eceef0"/>
        <stop offset="1" stop-color="#ffffff"/>
      </linearGradient>
      <linearGradient id="riverScene" x1="0" y1="0" x2="0" y2="1">
        <stop offset="0" stop-color="#8fc4e8"/>
        <stop offset="0.35" stop-color="#5f8fb8"/>
        <stop offset="0.6" stop-color="#7fa03c"/>
        <stop offset="0.75" stop-color="#6d7a55"/>
        <stop offset="1" stop-color="#3f5a5e"/>
      </linearGradient>
    </defs>

    <rect class="page" x="92" y="260" width="1308" height="932" fill="#ffffff"/>

    <rect class="back-skyline" x="92" y="500" width="653" height="400" fill="url(#skylineFade)" role="img" aria-label="Faint greyscale city skyline at dusk above a river bridge"/>

    <rect class="front-photo" x="745" y="430" width="655" height="500" fill="url(#riverScene)" role="img" aria-label="City high-rise towers and riverside trees along a river with ferries"/>

    <path class="front-base" d="M745,915 Q1100,925 1400,855 L1400,1152 L745,1152 Z" fill="#ffffff"/>
    <path class="front-rule-slate" d="M745,938 Q1100,942 1400,868 L1400,893 Q1100,955 745,948 Z" fill="var(--slate)"/>
    <path class="front-rule-sky" d="M745,912 Q1100,922 1400,852" fill="none" stroke="var(--sky)" stroke-width="9"/>

    <path class="top-rule-sky" d="M110,266 C400,430 700,510 900,514 C1100,518 1300,468 1400,428" fill="none" stroke="var(--sky)" stroke-width="8"/>
    <path class="top-band" d="M140,260 C420,410 700,492 900,498 C1100,502 1300,456 1400,416 L1400,260 Z" fill="var(--slate)"/>

    <rect class="footer-band" x="92" y="1152" width="1308" height="40" fill="var(--slate)"/>
  </svg>

  <p class="brand-name brand-name--front">APG</p>
  <p class="brand-name brand-name--back">APG</p>

  <div class="contact">
    <p class="contact-phone">
      <svg width="10" height="10" viewBox="0 0 24 24"><path d="M6.6 10.8a15 15 0 0 0 6.6 6.6l2.2-2.2c.3-.3.7-.4 1-.2 1.1.4 2.3.6 3.6.6.6 0 1 .4 1 1V20c0 .6-.4 1-1 1A17 17 0 0 1 3 4c0-.6.4-1 1-1h3.5c.6 0 1 .4 1 1 0 1.3.2 2.5.6 3.6.1.3 0 .7-.2 1z" fill="var(--sky)"/></svg>0198765432
    </p>
    <div class="contact-row">
      <svg width="13" height="12" viewBox="0 0 24 22"><rect x="1" y="4" width="22" height="16" rx="2" fill="var(--sky)"/><path d="M2 5l10 8 10-8" fill="none" stroke="#fff" stroke-width="2"/></svg>
      <span>info@alderpropertygroup.com.au</span>
    </div>
    <div class="contact-row">
      <svg width="12" height="16" viewBox="0 0 24 32"><path d="M12 1C6 1 2 5.5 2 11c0 7.5 10 20 10 20s10-12.5 10-20C22 5.5 18 1 12 1z" fill="var(--sky)"/><circle cx="12" cy="11" r="4" fill="#fff"/></svg>
      <span>Riverton and surrounding suburbs<br>through to the Coastal Peninsula</span>
    </div>
  </div>

  <h1 class="headline">
    <span class="headline-line">Quality Service</span>
    <span class="headline-line headline-line--accent">With Integrity</span>
  </h1>

  <p class="footer-url footer-url--back">www.alderpropertygroup.com.au</p>
  <p class="footer-url footer-url--front">www.alderpropertygroup.com.au</p>
</div>
</body>
</html>
```